Policy Manual in Education

I need the attached document to be put in a publishable format, with graphics a professional layout, and something that looks more like a professional report, etc. Use color samples from http://www.brqa-tz.com/ and www.kv7lm.com, my company is Kv7lm, we were hired to write the report and we also built the BRQA resource center http://www.brqa-tz.com/ .

Target Market(s)

Education

Requirements
Must have
• Look and feel around NM. http://www.brqa-tz.com/ and www.kv7lm.com

```html
<!DOCTYPE html>
<html lang="en">
<head>
<meta charset="utf-8">
<title>Policy Manual Layout</title>
<link rel="stylesheet" href="https://fonts.googleapis.com/css2?family=Open+Sans:wght@400;600;700&family=Montserrat:wght@400;500&display=swap">
<style>
:root{
  --bg:#a9a9a9;
  --paper:#ffffff;
  --navy:#1b3358;
  --blue:#1c5a9c;
  --sky:#3f84c4;
  --orange:#f6a21d;
  --ink:#333333;
  --rule:#8fb3d9;
  --row:#e4e8ee;
}
*{margin:0;padding:0;box-sizing:border-box}
html,body{width:1200px;height:1200px;overflow:hidden;background:var(--bg)}
body{position:relative;font-family:"Open Sans",Arial,sans-serif;color:var(--ink)}
.page{position:absolute;width:260px;height:350px;background:var(--paper);overflow:hidden;box-shadow:0 1px 3px rgba(0,0,0,.25)}
.page-title{position:absolute;top:22px;left:29px;right:29px;text-align:center;font-family:"Montserrat",Arial,sans-serif;font-size:8.6px;letter-spacing:.2px;color:#222;padding-bottom:2px;border-bottom:.7px solid var(--rule)}
.content{position:absolute;top:44px;left:26px;right:26px}
.h2{font-size:6.6px;font-weight:600;color:var(--blue);margin:5px 0 2px}
.h3{font-size:3.9px;color:var(--blue);margin:3px 0 1px}
.body{font-size:3.7px;line-height:1.55;color:var(--ink);margin-bottom:3px}
.lead{font-size:3.9px;line-height:1.5;color:var(--blue);margin-bottom:4px}
.accent{color:var(--blue)}
.footer{position:absolute;left:0;right:0;bottom:0;height:12px}
.footer svg{position:absolute;left:0;top:0}
.footer .site{position:absolute;left:24px;top:4.5px;font-size:3.2px;color:var(--navy);font-weight:600}
.footer .brand{position:absolute;left:100px;top:4px;font-family:"Open Sans",Arial,sans-serif;font-weight:700;font-size:4px;color:var(--navy)}
.footer .num{position:absolute;right:24px;top:4px;font-size:4px;color:var(--blue)}
.photo{position:absolute}
.toc-head{font-size:6.6px;font-weight:700;color:var(--blue);margin-bottom:6px}
.toc-row{display:flex;align-items:baseline;font-size:3.7px;margin-bottom:3.1px}
.toc-row .dots{flex:1;border-bottom:.5px dotted #777;margin:0 3px}
.cover .brand{position:absolute;font-family:"Open Sans",Arial,sans-serif;font-weight:700;color:var(--navy);line-height:1;white-space:nowrap}
.contact{position:absolute;top:305px;left:103px;font-size:2.9px;line-height:1.6;color:var(--blue)}
.contact.addr{left:156px;padding-left:4px;border-left:.5px solid var(--blue)}
.dot{display:inline-block;width:3px;height:3px;border-radius:50%;background:var(--blue);margin-right:2px;vertical-align:middle}
.callout{display:flex;align-items:center;background:var(--navy);color:#fff;font-size:4.3px;line-height:1.3;margin-bottom:5px}
.callout .icon{width:18px;height:22px;background:var(--orange);display:flex;align-items:center;justify-content:center;margin-right:4px;flex-shrink:0}
ul.list{list-style:none;font-size:3.7px;line-height:1.55;margin-bottom:3px}
ul.list li::before{content:"■ ";color:var(--navy)}
ul.sub{list-style:none;margin-left:18px;font-size:3.7px;line-height:1.55;color:var(--blue);margin-bottom:3px}
ul.sub li::before{content:"▶ ";color:var(--navy)}
table.grid{width:100%;border-collapse:separate;border-spacing:1px;font-size:3.3px;margin:5px 0}
table.grid th{background:var(--blue);color:#fff;font-weight:600;padding:1px}
table.grid td{background:var(--row);padding:.8px 3px}
table.grid td.c{text-align:center}
table.grid tr.phase td{color:var(--blue);font-weight:600;background:#d5dde8}
table.grid tr.total td{font-weight:700}
table.grid tr.grand td{background:var(--sky);color:#fff;font-weight:700}
</style>
</head>
<body>

<section class="page cover" style="left:35px;top:22px">
  <svg width="260" height="350" role="img" aria-label="Blue gradient field with faint triangle pattern above an orange diagonal band">
    <defs>
      <linearGradient id="coverBlue" x1="0" y1="0" x2="0" y2="1">
        <stop offset="0" stop-color="#1e5fa0"/>
        <stop offset="1" stop-color="#1b3358"/>
      </linearGradient>
    </defs>
    <polygon points="0,0 260,0 260,190 0,268" fill="url(#coverBlue)"/>
    <polygon points="0,268 260,190 260,236 0,283" fill="#f6a21d"/>
  </svg>
  <div class="brand" style="left:47px;top:309px;font-size:6px">Northvale Schools</div>
  <div class="contact"><span class="dot"></span>000-555-0142 Ext 210<br><span class="dot"></span>info@kv7lm.com<br><span class="dot"></span>www.kv7lm.com</div>
  <div class="contact addr">410, 2200 North Ridge Avenue<br>Riverside City, Northland 0000</div>
</section>

<section class="page" style="left:316px;top:22px">
  <div class="page-title">TABLE OF CONTENTS</div>
  <div class="content" style="top:50px;left:29px;right:29px">
    <div class="toc-head">Contents</div>
    <div class="toc-row"><span>Table of Contents</span><span class="dots"></span><span>01</span></div>
    <div class="toc-row"><span>Executive Summary</span><span class="dots"></span><span>02</span></div>
    <div class="toc-row"><span>Our Understanding of Your Needs</span><span class="dots"></span><span>02</span></div>
    <div class="toc-row"><span>Our Recommendations</span><span class="dots"></span><span>03</span></div>
    <div class="toc-row"><span>Our Approach</span><span class="dots"></span><span>05</span></div>
    <div class="toc-row"><span>Budget and Timeframe</span><span class="dots"></span><span>07</span></div>
    <div class="toc-row"><span>Appendix A: About Cedar Brook</span><span class="dots"></span><span>10</span></div>
    <div class="toc-row"><span>Appendix B: Selected Client List</span><span class="dots"></span><span>10</span></div>
    <div class="toc-row"><span>Appendix C: Our Capabilities</span><span class="dots"></span><span>11</span></div>
    <div class="toc-row"><span>Appendix D: Our Process</span><span class="dots"></span><span>12</span></div>
  </div>
  <footer class="footer"><svg width="260" height="12"><polygon points="0,0 86,0 96,12 0,12" fill="#f6a21d"/><polygon points="82,0 88,0 98,12 92,12" fill="#1b3358"/></svg><span class="site">www.sample-site.org</span><span class="brand">Northvale Schools</span><span class="num">1</span></footer>
</section>

<section class="page" style="left:610px;top:22px">
  <div class="page-title">HEADLINE HERE</div>
  <div class="content">
    <div class="h2">Solution</div>
    <div class="h3">AI automated accounting</div>
    <p class="body">Tallyra builds automation in stages on top of its current system to reach full automation thanks to the Tallyra AI. Tallyra AI automates every manual task performed by the user. It starts by connecting to all sources of accounting data such as bank accounts, credit cards, webshop or document storage systems. Based on these data, Tallyra AI creates bookings and generates financial reports. Finally, Tallyra AI features a chat-like interface that allows users to communicate seamlessly with it, viewing it as a trusted advisor over time for all their accounting queries.</p>
    <div class="h3">Blockchain software license or Token-as-a-License (TaaL)</div>
    <p class="body">It is possible to create tokens on blockchain that represent software licenses, also known as Token-as-a-Licence. Tallyra creates TaaL by using the Kestrel official wallet which interacts with the Kestrel blockchain. Upon purchase of TaaL, the token holder is free to transfer or sell TaaL using secondary market that is built directly over the blockchain, in our case, the Kestrel marketplace. Tallyra checks the validity of a token against the blockchain ensuring that token holders have access to the software. TaaL make distribution and securisation of software licenses easier for software developers. It also makes the management and resale of software license easier for software owners. All in all, TaaL has a higher value as a normal software license.</p>
    <div class="h2">Pre-ICO Token sale</div>
    <p class="body">To realize this innovative vision, Tallyra is launching a pre-ICO in form of a token sale on Kestrel blockchain. 20,000,000 tokens are available to purchase for the price of CHF 0.10 each during a 30-day period to be announced. Tokens represent Tallyra lifelong software licenses and by purchasing enough tokens, holders gain access to Tallyra software. 15,000 tokens give access to Tallyra invoicing or accounting. 20,000 tokens give access to both Tallyra accounting and invoicing. Future customers will still have the opportunity to buy directly yearly or monthly subscriptions to have access to Tallyra.</p>
    <div class="h2">Future plans</div>
    <p class="body">A future ICO is planned between 18 and 24 months after the pre-ICO token sale. This offering will support the development of Tallyra into a fully decentralized, privacy-focused ecosystem of applications. The new model will reward each participant so that a new world with zero administrative tasks becomes reality.</p>
  </div>
  <footer class="footer"><svg width="260" height="12"><polygon points="0,0 86,0 96,12 0,12" fill="#f6a21d"/><polygon points="82,0 88,0 98,12 92,12" fill="#1b3358"/></svg><span class="site">www.sample-site.org</span><span class="brand">Northvale Schools</span><span class="num">2</span></footer>
</section>

<section class="page" style="left:904px;top:22px">
  <div class="page-title">HEADLINE HERE</div>
  <div class="photo" role="img" aria-label="Photo of chess pieces on a board in warm light" style="left:29px;top:43px;width:210px;height:88px;background:linear-gradient(135deg,#3a2414,#b0763c 55%,#5a3a20)"></div>
  <div class="content" style="top:138px;left:29px;right:21px">
    <p class="lead">Tallyra's mission is to help and support the self-employed and small business owners with their administrative tasks so they can focus on what matters — their business.</p>
    <p class="body">Administrative tasks are cumbersome, time-consuming and often prevent small owners from focusing their time and energy on their business and their customers. They can also be extremely stressful and nerve-wracking for those attempting these tasks for the first time.</p>
    <p class="body">At Tallyra, we envisage accounting for the self-employed and small business owners as being <span class="accent">automated and decentralized</span></p>
    <p class="body">Accounting can and should be done automatically. By connecting to all sources of accounting data such as bank accounts, payment systems, e-commerce websites, and invoicing systems, Tallyra AI automatically completes these tasks, which would take hours to do manually. Bookings are created automatically and fully completed. Financial statements are available within a couple of clicks, and after analysing your data, Tallyra AI will offer you tips to improve your financial stability.</p>
    <p class="body">What may seem like a pipedream to the millions of self-employed who struggle with their admin, is already a reality. Now is the time to join Tallyra on its mission to transform the world of bookkeeping through the power of AI</p>
    <div class="h2">The Tallyra model</div>
    <p class="body">Tallyra is based on an innovative license model that uses Token-as-a-License (TaaL). The token represents lifelong software license for Tallyra solutions. The Pre-ICO token sales will enable Tallyra to complete its development of Tallyra AI to deliver fully automatic bookkeeping.</p>
    <p class="body">with leading edge business data access to ensure you have the best available data at your fingertips.</p>
  </div>
  <footer class="footer"><svg width="260" height="12"><polygon points="0,0 86,0 96,12 0,12" fill="#f6a21d"/><polygon points="82,0 88,0 98,12 92,12" fill="#1b3358"/></svg><span class="site">www.sample-site.org</span><span class="brand">Northvale Schools</span><span class="num">7</span></footer>
</section>

<section class="page" style="left:35px;top:407px">
  <div class="page-title">HEADLINE HERE</div>
  <div class="photo" role="img" aria-label="Photo of cupped hands holding a young seedling in soil" style="left:26px;top:44px;width:92px;height:129px;background:linear-gradient(160deg,#6b5a3f,#3c3020 60%,#2a2216)"></div>
  <div class="photo" role="img" aria-label="Photo of a blank sheet and a coffee cup on a wooden desk" style="left:26px;top:197px;width:92px;height:117px;background:linear-gradient(160deg,#7a3f1e,#a86432 50%,#4a2512)"></div>
  <div class="content" style="top:43px;left:130px;right:26px">
    <p class="lead">Tallyra's mission is to help and support the self-employed and small business owners with their administrative tasks so they can focus on what matters — their business.</p>
    <p class="body">Administrative tasks are cumbersome, time-consuming and often prevent small owners from focusing their time and energy on their business and their customers. They can also be extremely stressful and nerve-wracking for those attempting these tasks for the first time.</p>
    <p class="body">At Tallyra, we envisage accounting for the self-employed and small business owners as being <span class="accent">automated and decentralized</span></p>
    <p class="body">Accounting can and should be done automatically. By connecting to all sources of accounting data such as bank accounts, payment systems, e-commerce websites, and invoicing systems, Tallyra AI automatically completes these tasks, which would take hours to do manually. Bookings are created automatically and fully completed. Financial statements are available within a couple of clicks, and after analysing your data, Tallyra AI will offer you tips to improve your financial stability.</p>
    <p class="body">What may seem like a pipedream to the millions of self-employed who struggle with</p>
    <div class="h2">The Tallyra model</div>
    <p class="body">Tallyra is based on an innovative license model that uses Token-as-a-License (TaaL). The token represents lifelong software license for Tallyra solutions. The Pre-ICO token sales will enable Tallyra to complete its development of Tallyra AI to deliver fully automatic bookkeeping.</p>
  </div>
  <footer class="footer"><svg width="260" height="12"><polygon points="0,0 86,0 96,12 0,12" fill="#f6a21d"/><polygon points="82,0 88,0 98,12 92,12" fill="#1b3358"/></svg><span class="site">www.sample-site.org</span><span class="brand">Northvale Schools</span><span class="num">8</span></footer>
</section>

<section class="page" style="left:319px;top:407px">
  <div class="page-title">VISION</div>
  <div class="content" style="top:45px">
    <div class="callout">
      <span class="icon"><svg width="12" height="12" viewBox="0 0 12 12"><circle cx="6" cy="6" r="5" fill="none" stroke="#fff" stroke-width="1"/><circle cx="6" cy="6" r="2.6" fill="none" stroke="#fff" stroke-width="1"/><circle cx="6" cy="6" r=".9" fill="#fff"/></svg></span>
      <span>Tallyra's mission is to help and support the self-employed and small business owners with their administrative tasks so they can focus on what matters — their business.</span>
    </div>
    <p class="lead">Administrative tasks are cumbersome, time-consuming and often prevent small owners from focusing their time and energy on their business and their customers. They can also be extremely stressful and nerve-wracking for those attempting these tasks for the first time.</p>
    <p class="body" style="text-align:center">At Tallyra, we envisage accounting for the self-employed and small business owners as being<br><span class="accent">automated and decentralized</span></p>
    <p class="body">Accounting can and should be done automatically. By connecting to all sources of accounting data such as bank accounts, payment systems, e-commerce websites, and invoicing systems, Tallyra AI automatically completes these tasks, which would take hours to do manually. Bookings are created automatically and fully completed. Financial statements are available within a couple of clicks, and after analysing your data, Tallyra AI will offer you tips to improve your financial stability.</p>
    <p class="body">What may seem like a pipedream to the millions of self-employed who struggle with their admin, is already a reality. Now is the time to join Tallyra on its mission to transform the world of bookkeeping through the power of AI</p>
    <div class="h2">The Tallyra model</div>
    <p class="body">Tallyra is based on an innovative license model that uses Token-as-a-License (TaaL). The token represents lifelong software license for Tallyra solutions. The Pre-ICO token sales will enable Tallyra to complete its development of Tallyra AI to deliver fully automatic bookkeeping.</p>
    <p class="body">The Pre-ICO token sale will also pave the way for a future Tallyra ICO. Tallyra will launch accounting on the blockchain and ensure your accounting data is comprehensive and private, but available everywhere within your preferred apps. It will empower you to manage your data as you see fit in a fully decentralized way. Furthermore, a new range of business apps will connect to Tallyra to provide you</p>
    <p class="body">with leading edge business data access to ensure you have the best available data at your fingertips.</p>
    <p class="body">Tallyra supports strong data ownership laws that truly protect individuals and ensure they have complete ownership of their data. Through decentralisation Tallyra helps to ensure you always have full ownership of your data to decide how it should be used.</p>
    <p class="body">To find out more about the Tallyra AI project, and the Tallyra TaaL, or if you are interested in purchasing Tallyra TaaL, please register with your email at <span class="accent" style="text-decoration:underline">www.kv7lm.com/ico</span> so we</p>
  </div>
  <footer class="footer"><svg width="260" height="12"><polygon points="0,0 86,0 96,12 0,12" fill="#f6a21d"/><polygon points="82,0 88,0 98,12 92,12" fill="#1b3358"/></svg><span class="site">www.sample-site.org</span><span class="brand">Northvale Schools</span><span class="num">3</span></footer>
</section>

<section class="page" style="left:610px;top:407px">
  <div class="page-title">OUR UNDERSTANDING OF YOUR NEEDS</div>
  <div class="content" style="top:45px">
    <p class="body">In the last two weeks of January 2014 we conducted high level conversations both with your staff and your technology partner BrightRelay. As a result of those conversations we've been able to gather the following high level goals for your project:</p>
    <p style="font-size:5.6px;color:#777;line-height:1.25;margin:4px 0">CloudLedger must be in place to support StepWell at launch and as the program evolves</p>
    <p class="body accent" style="font-weight:700">The most critical aspect of this implementation both in terms of time sensitivity as well as functionality is centered around the support for the StepWell project. Our current understanding of this project and how it relates to CloudLedger is as follows:</p>
    <ul class="list">
      <li>StepWell will be comprised of a series of websites focused on organizing institutions and individuals within six specific community sectors with the goal of increased institutional and public support to help the region be better prepared to minimize the risks and maximize opportunities of changing climate.</li>
      <li>The primary goals of the CRM application are:</li>
    </ul>
    <ul class="sub">
      <li>capture information of individuals and organizations (along with their respective roles)</li>
      <li>track their progress on their site specific to-do lists and site interactions</li>
      <li>allow greenNation to push out next steps (ideally in an automated style) related to their to-do list progress and online interactions</li>
      <li>infuse greenNation's online and offline marketing program with useful segmentation information</li>
      <li>natively integrate with both the StepWell family of sites as well as greenNation's email service provider of choice</li>
    </ul>
    <ul class="list"><li>The data architecture must be well defined but flexible to support the core needs of the sites as launch as well as anticipated needs in the future.</li></ul>
    <ul class="sub">
      <li>For instance, the faith based site may collect a "denomination" field, while other sites may not collect that field.</li>
      <li>Future interactions outside of the to-do list may become necessary to track and greenNation will need a systemic way to capture those interactions, be able to segment on them and potentially provide automated marketing around those similar to the to-do list</li>
    </ul>
    <ul class="list"><li>The information collected from the StepWell sites must be combined with current information held within greenNation and provide a holistic view of institutions and individuals.</li></ul>
  </div>
  <footer class="footer"><svg width="260" height="12"><polygon points="0,0 86,0 96,12 0,12" fill="#f6a21d"/><polygon points="82,0 88,0 98,12 92,12" fill="#1b3358"/></svg><span class="site">www.sample-site.org</span><span class="brand">Northvale Schools</span><span class="num">6</span></footer>
</section>

<section class="page" style="left:905px;top:407px">
  <div class="page-title">BUDGET AND TIMEFRAME</div>
  <div class="content" style="top:44px;left:29px;right:25px">
    <div class="h2" style="margin-top:0">Implementation Estimate</div>
    <p class="body">The bulk of the implementation costs will be defined by discovery. Based on similar CRM implementation projects, we feel expect that the CRM side will be somewhere between 200 and 300 hours, give or take. The wide swing in hours in phase one is related to the ill-defined nature of both the integration needs and our role in the integration project. Our focus in discovery will be to nail down those requirements and our role as it relates to what is needed to integrate the sites with the CRM.</p>
    <table class="grid">
      <tr><th style="width:52%">Task</th><th>Hours</th><th>Cost</th></tr>
      <tr><td>Discovery</td><td class="c">40</td><td class="c">$8,000</td></tr>
      <tr class="phase"><td>Phase 1</td><td></td><td></td></tr>
      <tr><td>Discovery</td><td class="c">20-40</td><td class="c">$8,000</td></tr>
      <tr><td>Discovery</td><td class="c">20-40</td><td class="c">$8,000</td></tr>
      <tr><td>Discovery</td><td class="c">20-40</td><td class="c">$8,000</td></tr>
      <tr class="total"><td>Total Phase 1</td><td class="c">80-240</td><td class="c">$16,800-40,000</td></tr>
      <tr class="phase"><td>Phase 2</td><td></td><td></td></tr>
      <tr><td>Discovery</td><td class="c">20-40</td><td class="c">$8,000</td></tr>
      <tr class="total"><td>Total Phase 2</td><td class="c">80-240</td><td class="c">$16,800-40,000</td></tr>
      <tr class="grand"><td>Total Estimated Implementation Cost</td><td class="c">220-480</td><td class="c" style="background:var(--blue)">$44,000-96,000</td></tr>
    </table>
    <div class="h2" style="margin-top:9px">Project Timeline</div>
    <p class="body">Based on the information we have out our disposal, the March 21st launch date doesn't seem a realistic goal to get both the work done needed to provide the foundation for the future CRM instance and the integration given the state of apparent flux of the requirements. That said, we feel it prudent to proceed with discovery before committing to or pushing that date. We are currently estimating that the first phase will take somewhere between 7 and 12 weeks (including discovery) to complete.</p>
    <table class="grid">
      <tr><th style="width:64%">Task</th><th>Weeks to Complete</th></tr>
      <tr><td>Discovery</td><td class="c">1-2</td></tr>
      <tr><td>Phase 1</td><td class="c">6-10</td></tr>
      <tr><td>Phase 2</td><td class="c">8-12</td></tr>
      <tr class="total"><td>Total Number of Weeks</td><td></td></tr>
    </table>
  </div>
  <footer class="footer"><svg width="260" height="12"><polygon points="0,0 86,0 96,12 0,12" fill="#f6a21d"/><polygon points="82,0 88,0 98,12 92,12" fill="#1b3358"/></svg><span class="site">www.sample-site.org</span><span class="brand">Northvale Schools</span><span class="num">5</span></footer>
</section>

<section class="page cover" style="left:36px;top:810px">
  <svg width="260" height="350" role="img" aria-label="Blue gradient field with faint triangle pattern above an orange diagonal band">
    <defs>
      <linearGradient id="backBlue" x1="0" y1="0" x2="0" y2="1">
        <stop offset="0" stop-color="#1e5fa0"/>
        <stop offset="1" stop-color="#1b3358"/>
      </linearGradient>
    </defs>
    <polygon points="0,0 260,0 260,190 0,268" fill="url(#backBlue)"/>
    <polygon points="0,268 260,190 260,236 0,283" fill="#f6a21d"/>
  </svg>
  <div class="brand" style="left:117px;top:300px;font-size:12px">Northvale Schools</div>
</section>

</body>
</html>
```